Real Estate Marketing Company Needs 1 Page 8.5x11 Price List Flyer Design

We need a 1 page 8.5in x 11in price list flyer that is intended for drop off at local offices. This is intended to show all the services we offer including pricing to potential new clients. It should be separated into sections for the different services we offer. I'd also like some photos and our Logo on the list to make it look nice so its not all text. Try to incorporate the logo colors in the design.

Industry/Entity Type

Real Estate

Requirements
Must have
• Price List
• Photos
• Logo
• website address

```html
<!DOCTYPE html>
<html lang="en">
<head>
<meta charset="utf-8">
<title>Price List Flyer</title>
<link rel="stylesheet" href="https://fonts.googleapis.com/css2?family=Cinzel:wght@400;600&family=Open+Sans:wght@400;600;700&display=swap">
<style>
  :root {
    --brand-red: #a31c22;
    --band-grey: #a9a9a9;
    --bar-grey: #b3b3b3;
    --white: #ffffff;
    --ink: #1f1f1f;
  }
  * { margin: 0; padding: 0; box-sizing: border-box; }
  html, body { width: 927px; height: 1200px; overflow: hidden; background: var(--white); }
  .flyer { position: relative; width: 927px; height: 1200px; font-family: "Open Sans", Arial, sans-serif; color: var(--white); }

  .title-band { position: absolute; left: 0; top: 0; width: 927px; height: 84px; background: var(--band-grey); display: flex; align-items: center; justify-content: center; }
  .title-band h1 { font-family: "Cinzel", "Times New Roman", serif; font-weight: 600; font-size: 51px; letter-spacing: 1px; color: var(--white); white-space: nowrap; }
  .title-rule { position: absolute; left: 0; top: 84px; width: 927px; height: 7px; background: var(--brand-red); }

  .hero-photo { position: absolute; left: 0; top: 91px; width: 927px; height: 375px;
    background: linear-gradient(180deg, #6b93c9 0%, #a9c3e0 18%, #c9b79a 40%, #b8a07c 60%, #5f7a3d 80%, #4a9fc4 100%); }
  .photo-strip-rule { position: absolute; left: 0; top: 466px; width: 927px; height: 4px; background: var(--band-grey); }
  .photo-strip { position: absolute; left: 0; top: 470px; width: 927px; height: 150px; display: flex; gap: 2px; background: var(--band-grey); }
  .strip-photo { flex: 1; }
  .strip-photo.porch { background: linear-gradient(160deg, #6f8a45, #d9d5c8 55%, #b77a3c); }
  .strip-photo.great-room { background: linear-gradient(180deg, #d8d2c4, #f0ece4 50%, #5f5a52); }
  .strip-photo.living-room { background: linear-gradient(180deg, #e9e4d8, #efe7d6 45%, #a0552a); }
  .strip-photo.aerial { background: linear-gradient(160deg, #355c2a, #6f8a54 50%, #2e4f24); }

  .brand-tile { flex: 1; min-width: 0; background: var(--white); display: flex; flex-direction: column; align-items: center; justify-content: center; gap: 12px; text-align: center; }
  .brand-mark { width: 76px; height: 76px; border-radius: 50%; background: var(--brand-red); }
  .brand-name { font-family: "Open Sans", Arial, sans-serif; font-weight: 600; font-size: 16px; line-height: 20px; color: var(--ink); white-space: nowrap; text-align: center; }

  .price-panel { position: absolute; left: 0; top: 622px; width: 927px; height: 558px; background: var(--brand-red); }
  .foot-band { position: absolute; left: 0; top: 1180px; width: 927px; height: 20px; background: var(--band-grey); }

  .section-bar { position: absolute; height: 30px; background: var(--bar-grey); color: var(--white); font-weight: 700; font-size: 17px; display: flex; align-items: center; justify-content: center; }
  .col-left { left: 43px; width: 408px; }
  .col-right { left: 476px; width: 420px; }

  .price-list { position: absolute; list-style: none; font-size: 16px; line-height: 25px; white-space: nowrap; }
  .price-list b { font-weight: 700; }
  .price-list.tight { line-height: 29.5px; }
  .price-list.airy { line-height: 28px; }
  .note { position: absolute; font-size: 16px; line-height: 25px; }

  .contact { position: absolute; left: 0; top: 1100px; width: 927px; text-align: center; font-weight: 700; font-size: 21.5px; line-height: 33px; white-space: nowrap; }
</style>
</head>
<body>
<div class="flyer">
  <header class="title-band"><h1>Presentation Is Everything</h1></header>
  <div class="title-rule"></div>

  <div class="hero-photo" role="img" aria-label="Exterior of a stone luxury estate with pool, terrace and wicker chairs"></div>
  <div class="photo-strip-rule"></div>
  <div class="photo-strip">
    <div class="strip-photo porch" role="img" aria-label="Covered porch with wicker seating"></div>
    <div class="strip-photo great-room" role="img" aria-label="Bright great room with tall arched windows"></div>
    <div class="brand-tile">
      <div class="brand-mark"></div>
      <div class="brand-name">Open House Imaging</div>
    </div>
    <div class="strip-photo living-room" role="img" aria-label="Living room with white sofa and hardwood floor"></div>
    <div class="strip-photo aerial" role="img" aria-label="Aerial view of an estate among trees"></div>
  </div>

  <section class="price-panel"></section>

  <div class="section-bar col-left" style="top:648px">Package Pricing</div>
  <ul class="price-list col-left" style="top:686px">
    <li><b>Silver Package:</b> 15 Photos + Floor Plan</li>
    <li>(3,500 sqft) - $225</li>
    <li><b>Gold Package:</b> 25 Photos + Floor Plan</li>
    <li>(4,500 sqft) - $300</li>
    <li><b>Platinum Package:</b> 35 Photos + Floor Plan</li>
    <li>(5,500 sqft) - $375</li>
  </ul>

  <div class="section-bar col-left" style="top:851px">Photography Only</div>
  <ul class="price-list col-left" style="top:896px">
    <li>15 Photo Bundle: $100</li>
    <li>25 Photo Bundle: $150</li>
    <li>35 Photo Bundle: $200</li>
  </ul>

  <div class="section-bar col-left" style="top:985px">Additional Services</div>
  <ul class="price-list col-left" style="top:1030px">
    <li><b>Aerial Photos:</b> 3-6 Photos - $200</li>
    <li>($75 if combined with another package)</li>
  </ul>

  <ul class="price-list airy col-right" style="top:643px">
    <li><b>Aerial Video:</b> (1-3 min video) - $375</li>
    <li><b>Branded Video Tour w/ Aerial Video:</b></li>
    <li>(2-4 min video of property) - $800-$1300</li>
    <li>(voiceover optional, call for details)</li>
    <li><b>Twilight Photos:</b> 3-6 Photos - $225</li>
    <li><b>Luxury Package:</b> $2,000 (includes all services listed</li>
  </ul>

  <div class="section-bar col-right" style="top:821px; width:408px">Floor Plans</div>
  <ul class="price-list tight col-right" style="top:865px">
    <li>Floor Plan (3,500 sqft) - $150</li>
    <li>Floor Plan (4,500 sqft) - $175</li>
    <li>Floor Plan (5,500 sqft) - $200</li>
    <li>*$25 per additional 500sqft</li>
  </ul>
  <p class="note col-right" style="top:1006px">**Complex floor plans are priced individually<br>regardless of sqft.</p>

  <p class="contact">For more information or to book a shoot please visit our website:<br>www.OpenHouseImaging.com or call Daniel at 555-014-2290</p>

  <div class="foot-band"></div>
</div>
</body>
</html>
```